A4 6 page tri-fold brochure for security screen company

Brochure design and layout for a new company based in the UAE called Harbor Panes. We make clear mesh security screen doors and windows that aesthetically blend with the house, like a fly screen, rather than a traditional heavy looking security screen. We want to project an image of safety and security but with warmth and humanity to it, not just something clinical. Copy hasn't been written yet so use dummy text or pull and adjust copy form our website www.harborpanes-example.ae.
Target market: home owners, financially comfortable, possibly with young children or pets.
Purpose of brochure: to have potential clients contact us (via phone, whatsapp, email or through our website) to arrange a free measure and quote.
More details provided in attached word doc brief and product images, logos etc, attached also.
Please see attached brief.

Target Market(s)

Home owners, financially comfortable, possibly with young children or pets.

Industry/Entity Type

Home Improvement

Font styles to use
Serif
Sans Serif

Colors
0255a3
3176b5
85acd3
cfdfed
eaf1f7

Requirements
Must have
• Good clear images with detailed close ups (or call outs) of specific details such as the mesh and locks.
• Contact details to include website www.harborpanes-example.ae, phone number: +971 50 318 2097, email address: oliver@harborpanes-example.ae
Nice to have
• If your are comfortable using and adjusting the appropriate copy from our website please do so.
• Images - I've included a lot of images so please choose the most appropriate to help sell the product. Some of the better images I like are: _DSC2929, French_Windows, HARBOR_PANES-3204, HARBOR_PANES-3231, HARBOR_PANES-3345, HARBOR_PANES-3354, HARBOR_PANES-3401, Girls room windows1, Girls room windows2, IMG_2968. Please don't limit yourself to these images and use the ones you feel best fit.
Should not have
• Please see attached brief.

```html
<!DOCTYPE html>
<html lang="en">
<head>
<meta charset="utf-8">
<title>Harbor Panes – Tri-fold Brochure</title>
<link rel="stylesheet" href="https://fonts.googleapis.com/css2?family=Open+Sans:ital,wght@0,400;0,600;0,700;0,800;1,400;1,600&display=swap">
<style>
:root{
  --navy:#0255a3;
  --blue:#3176b5;
  --sky:#85acd3;
  --mist:#cfdfed;
  --ice:#eaf1f7;
  --ink:#1d1f22;
  --charcoal:#2a2c30;
  --text:#4a4d52;
  --page:#e3e3e3;
  --white:#ffffff;
}
*{box-sizing:border-box;margin:0;padding:0}
html,body{width:1200px;height:2400px;overflow:hidden}
body{background:var(--page);font-family:"Open Sans",Arial,sans-serif;color:var(--text);position:relative}
.spread{position:absolute;left:60px;width:1080px;height:764px;display:flex;box-shadow:0 18px 40px rgba(0,0,0,.22);background:var(--white)}
.spread--outside{top:356px}
.spread--inside{top:1280px}
.panel{position:relative;width:360px;height:100%;overflow:hidden;background:var(--white)}
.panel + .panel{border-left:1px solid #d8dde3}
.photo{position:absolute;left:0;width:100%}
.footer{position:absolute;left:0;bottom:0;width:100%;height:40px;display:flex;align-items:center;justify-content:center;font-weight:700;font-size:13px;letter-spacing:.5px;color:var(--white)}
.footer--blue{background:linear-gradient(90deg,var(--navy),var(--blue))}
.footer--dark{background:var(--ink);border-top:4px solid var(--blue)}
.footer--flap{justify-content:flex-start;padding-left:20px}

/* logo */
.logo{display:flex;align-items:center;gap:10px;font-weight:800;letter-spacing:2px;text-transform:uppercase}
.logo__mark{width:26px;height:26px;background:var(--blue)}
.logo--light{color:var(--white);font-size:26px}
.logo--blue{color:var(--navy);font-size:19px}

/* outside flap */
.flap__dark{position:absolute;top:220px;left:0;width:100%;height:504px;background:var(--charcoal);padding:22px 22px}
.flap__lead{font-style:italic;font-size:12.5px;line-height:1.5;color:var(--sky);margin-bottom:12px}
.feature-list{list-style:none}
.feature-list li{font-size:11.5px;color:#d9dde2;line-height:1.9;display:flex;align-items:center;gap:8px}
.feature-list svg{flex:none}
.thumbs{position:absolute;left:22px;right:22px;bottom:36px;display:grid;grid-template-columns:1fr 1fr;gap:8px}
.thumb{height:84px}

/* back panel */
.panel--back{background:linear-gradient(180deg,var(--white) 0%,var(--ice) 100%);padding:30px 30px 0;text-align:center}
.panel--back .logo{justify-content:center;margin-bottom:18px}
.tagline{font-weight:800;font-size:14px;color:var(--ink);margin-bottom:14px;letter-spacing:.2px}
.body-copy{font-size:10.5px;line-height:1.6;text-align:left;margin-bottom:10px}
.badge-row{display:flex;align-items:center;gap:12px;margin:10px 0 12px;text-align:left}
.badge{flex:none;width:64px;height:64px;border-radius:50%;background:radial-gradient(circle,#3a3a3a 55%,#c9a248 57%,#e2c26a 70%,#a8842e 100%)}
.badge-row p{font-size:9.5px;line-height:1.5;font-style:italic}
.invite{font-size:12px;font-style:italic;font-weight:600;color:var(--ink);line-height:1.5;margin-bottom:12px}
.cta{font-weight:800;font-size:15px;color:var(--ink);margin-bottom:10px}
.phone-pill{display:inline-flex;align-items:center;gap:10px;padding:7px 22px;border-radius:18px;background:linear-gradient(90deg,var(--navy),var(--blue));color:var(--white);font-weight:700;font-size:14px}
.social{display:flex;justify-content:center;gap:8px;margin-top:10px}
.social span{width:16px;height:16px;border-radius:50%;background:var(--blue)}

/* front cover */
.cover__top{position:absolute;top:0;left:0;width:100%;height:150px}
.cover__top .logo{position:absolute;top:44px;left:0;width:100%;justify-content:center}
.cover__photo{top:132px;height:430px;background:linear-gradient(160deg,#dfe3e6 0%,#b9c3c0 40%,#7e9a6d 70%,#c24a8c 100%)}
.mesh-callout{position:absolute;top:470px;right:16px;width:104px;height:104px;border-radius:50%;border:5px solid var(--white);box-shadow:0 4px 10px rgba(0,0,0,.3);background:radial-gradient(circle,#555 0%,#2a2a2a 70%)}
.cover__headline{position:absolute;top:592px;left:0;width:100%;text-align:center;font-weight:800;font-size:17px;line-height:1.35;color:var(--ink);text-transform:uppercase;padding:0 24px}

/* inside */
.inside__photo{top:0;height:238px}
.section-band{position:absolute;top:238px;left:0;width:100%;background:var(--ink);padding:14px 22px 16px;color:#d4d8dd;font-size:10.5px;line-height:1.55}
.section-band h2{font-size:14px;font-weight:800;color:var(--blue);letter-spacing:.5px;margin-bottom:6px}
.inside__body{position:absolute;left:22px;right:22px;font-size:10.5px;line-height:1.6}
.inside__body h3{font-size:14px;font-weight:700;color:var(--ink);line-height:1.35;margin:6px 0 8px}
.product{display:flex;gap:8px;margin-bottom:9px}
.product__num{flex:none;width:16px;height:16px;border-radius:50%;background:var(--blue);color:var(--white);font-size:9px;font-weight:700;display:flex;align-items:center;justify-content:center;margin-top:2px}
.product h4{font-size:11.5px;font-weight:700;color:var(--navy)}
.product p{font-size:10px;line-height:1.45}
.thumb-row{position:absolute;left:22px;right:22px;bottom:56px;display:flex;gap:8px}
.thumb-row .thumb{flex:1;height:78px}
</style>
</head>
<body>

<!-- Outside spread -->
<section class="spread spread--outside">

  <article class="panel panel--flap">
    <div class="photo" style="top:0;height:220px;background:linear-gradient(180deg,#8fb9dc 0%,#cfe1ee 45%,#e8dcc4 70%,#b9a88a 100%)" role="img" aria-label="Two-storey villa with screened windows and doors"></div>
    <div class="flap__dark">
      <p class="flap__lead">Each Harbor Panes screen is designed and engineered to provide superior protection for your family and home.</p>
      <ul class="feature-list">
        <li><svg width="10" height="10" viewBox="0 0 10 10"><path d="M1 5l3 3 5-6" stroke="#3176b5" stroke-width="2" fill="none"/></svg>Patented fixing method</li>
        <li><svg width="10" height="10" viewBox="0 0 10 10"><path d="M1 5l3 3 5-6" stroke="#3176b5" stroke-width="2" fill="none"/></svg>Superior strength</li>
        <li><svg width="10" height="10" viewBox="0 0 10 10"><path d="M1 5l3 3 5-6" stroke="#3176b5" stroke-width="2" fill="none"/></svg>Security mesh</li>
        <li><svg width="10" height="10" viewBox="0 0 10 10"><path d="M1 5l3 3 5-6" stroke="#3176b5" stroke-width="2" fill="none"/></svg>Aluminium frame</li>
        <li><svg width="10" height="10" viewBox="0 0 10 10"><path d="M1 5l3 3 5-6" stroke="#3176b5" stroke-width="2" fill="none"/></svg>Locks and hardware</li>
        <li><svg width="10" height="10" viewBox="0 0 10 10"><path d="M1 5l3 3 5-6" stroke="#3176b5" stroke-width="2" fill="none"/></svg>Screws</li>
      </ul>
      <div class="thumbs">
        <div class="thumb" style="background:linear-gradient(135deg,#e9e4da,#8d8a83)" role="img" aria-label="Close-up of screen door lock"></div>
        <div class="thumb" style="background:linear-gradient(135deg,#c69b73,#6e4d33)" role="img" aria-label="Screen door frame detail"></div>
        <div class="thumb" style="background:linear-gradient(135deg,#a9b4bd,#4f5860)" role="img" aria-label="Stainless steel mesh close-up"></div>
        <div class="thumb" style="background:linear-gradient(135deg,#d9c2a6,#8a6c4f)" role="img" aria-label="Hinge and fixing detail"></div>
      </div>
    </div>
    <div class="footer footer--blue footer--flap">www.harborpanes-example.ae</div>
  </article>

  <article class="panel panel--back">
    <div class="logo logo--blue"><span class="logo__mark"></span>Harbor Panes</div>
    <p class="tagline">NO INTRUDERS, NO BUGS, NO WORRIES!</p>
    <p class="body-copy">Harbor Panes screens keep the bugs out and the breeze in, while quietly guarding your home. Strong enough to stop intruders, fine enough to leave the view untouched.</p>
    <p class="body-copy">Our screen doors and windows come in a range of colours and styles to suit your home. Each one is made to measure so it blends in with your windows and doors.</p>
    <p class="body-copy">With a 10 year warranty and custom sizes for your windows and doors, contact us today to arrange a free quote.</p>
    <div class="badge-row">
      <div class="badge" role="img" aria-label="Warranty seal"></div>
      <p>Product testing shows our mesh resists knife, impact and pry attacks, giving lasting peace of mind for your family.</p>
    </div>
    <p class="invite">Please feel free to contact us to arrange a free measure and quote. We look forward to protecting your assets.</p>
    <p class="cta">CONTACT US FOR A FREE QUOTE</p>
    <div class="phone-pill">
      <svg width="14" height="14" viewBox="0 0 24 24"><path fill="#fff" d="M6.6 10.8a15 15 0 006.6 6.6l2.2-2.2a1 1 0 011-.25 11.4 11.4 0 003.6.57 1 1 0 011 1V20a1 1 0 01-1 1A17 17 0 013 4a1 1 0 011-1h3.5a1 1 0 011 1c0 1.25.2 2.46.57 3.6a1 1 0 01-.25 1z"/></svg>
      +971 50 318 2097
    </div>
    <div class="social"><span></span><span></span><span></span></div>
    <div class="footer footer--dark">www.harborpanes-example.ae</div>
  </article>

  <article class="panel panel--cover">
    <svg class="cover__top" viewBox="0 0 360 150" preserveAspectRatio="none">
      <path d="M0 0H360V118Q180 160 0 118Z" fill="#1d1f22"/>
      <path d="M0 118Q180 160 360 118V126Q180 168 0 126Z" fill="#3176b5"/>
    </svg>
    <div class="cover__top"><div class="logo logo--light"><span class="logo__mark"></span>Harbor Panes</div></div>
    <div class="photo cover__photo" role="img" aria-label="Child looking out to the garden through a sliding screen door"></div>
    <div class="mesh-callout" role="img" aria-label="Close-up callout of woven stainless steel mesh"></div>
    <p class="cover__headline">Seriously strong screens that let the breeze in and keep intruders (and bugs) out!</p>
    <div class="footer footer--blue">www.harborpanes-example.ae</div>
  </article>

</section>

<!-- Inside spread -->
<section class="spread spread--inside">

  <article class="panel">
    <div class="photo inside__photo" style="background:linear-gradient(160deg,#e7ecef 0%,#9fb3c0 45%,#4a4f55 100%)" role="img" aria-label="Patio dining area with screened glass doors"></div>
    <div class="section-band">
      <h2>ABOUT US</h2>
      At Harbor Panes we came to work each day to solve a problem that bothered us for years: that was how to stop our fly screens from constantly breaking.
    </div>
    <div class="inside__body" style="top:352px">
      <h3>Super strong, stainless steel mesh security screens that look stylish and won't break.</h3>
      <p>Harbor Panes is a brand new initiative to the UAE. We custom make and install premium high grade stainless steel mesh screen doors and window screens in place of those flimsy fly screens we know drive you crazy.</p>
      <h3>Sleep easy, and enjoy the fresh winter breeze, knowing your loved ones are safe and secure.</h3>
      <p>Our mesh screens may look like ordinary insect screens, but the stainless steel mesh passes tough knife and impact tests. Manufactured using a patented framing system, the screens offer protection of steel, a barrier for bugs and an unobstructed view.</p>
    </div>
    <div class="footer footer--blue">www.harborpanes-example.ae</div>
  </article>

  <article class="panel">
    <div class="photo inside__photo" style="background:linear-gradient(160deg,#f1efea 0%,#c9c3b8 50%,#8c8377 100%)" role="img" aria-label="Bright living room with screen doors opening to the garden"></div>
    <div class="section-band">
      <h2>SCREEN DOORS</h2>
      Security screen doors are the perfect choice for protecting your family home.
    </div>
    <div class="inside__body" style="top:330px">
      <p style="margin-bottom:10px">The stainless steel mesh screens are secured in a patented aluminium frame to provide a lasting solution for high traffic areas and are stylish too.</p>
      <div class="product"><span class="product__num">1</span><div><h4>Sliding Screen Doors</h4><p>Sliding doors are a great choice for wide openings and patios.</p></div></div>
      <div class="product"><span class="product__num">2</span><div><h4>Hinged Screen Doors</h4><p>For front and back doors, we also offer a full range of hinged options.</p></div></div>
      <div class="product"><span class="product__num">3</span><div><h4>French Screen Doors</h4><p>Perfect for inward and outward opening doors that suit classic homes.</p></div></div>
    </div>
    <div class="thumb-row">
      <div class="thumb" style="background:linear-gradient(135deg,#d6cdbf,#7f7466)" role="img" aria-label="Sliding screen door"></div>
      <div class="thumb" style="background:linear-gradient(135deg,#e4d7d9,#a07a80)" role="img" aria-label="Hinged screen door"></div>
    </div>
    <div class="footer footer--dark">www.harborpanes-example.ae</div>
  </article>

  <article class="panel">
    <div class="photo inside__photo" style="background:linear-gradient(160deg,#f4f3f0 0%,#d8d3c8 50%,#9aa4a8 100%)" role="img" aria-label="Kitchen with screened sliding windows"></div>
    <div class="section-band">
      <h2>WINDOW SCREENS</h2>
      Harbor Panes custom mesh window screens are designed to protect all shapes and sizes of window openings.
    </div>
    <div class="inside__body" style="top:340px">
      <div class="product"><span class="product__num">1</span><div><h4>Sliding Screen Windows</h4><p>Slim sliding screens suit the modern window and keep it easy to open.</p></div></div>
      <div class="product"><span class="product__num">2</span><div><h4>French Screen Windows</h4><p>Made to fit both inward and outward opening windows.</p></div></div>
      <div class="product"><span class="product__num">3</span><div><h4>Fixed Window Screens</h4><p>A fixed frame for windows that need lasting, quiet protection.</p></div></div>
      <div class="product"><span class="product__num">4</span><div><h4>Hinged Screen Window</h4><p>Swing open screens that allow full access to the window.</p></div></div>
    </div>
    <div class="thumb-row">
      <div class="thumb" style="background:linear-gradient(135deg,#dfe3e6,#7d8a93)" role="img" aria-label="Screened window from inside"></div>
      <div class="thumb" style="background:linear-gradient(135deg,#f0c9d6,#b3677f)" role="img" aria-label="Child's bedroom with screened windows"></div>
      <div class="thumb" style="background:linear-gradient(135deg,#e6dfcf,#8f8571)" role="img" aria-label="Fixed window screen"></div>
    </div>
    <div class="footer footer--blue">www.harborpanes-example.ae</div>
  </article>

</section>

</body>
</html>
```